Trade Show Norvane 3x3 booth schel scheme

We would like to have full coverage design for 3x3 booth scheel

2x2 pop up Counter (1200mm wide x 900mm high x 400mm deep)
Our company provides food safety training, consultancy and food safety app service for hospitality businesses.

```html
<!DOCTYPE html>
<html lang="en">
<head>
<meta charset="utf-8">
<title>Norvane – Pop-up Counter Wrap</title>
<link rel="stylesheet" href="https://fonts.googleapis.com/css2?family=Montserrat:wght@400;500&family=Nunito:wght@800&display=swap">
<style>
  :root {
    --lime: #d3d731;
    --lime-light: #dde25a;
    --lime-deep: #c8cc22;
    --ink: #111111;
    --white: #ffffff;
    --stage: #ffffff;
    --guide: #6f6f6f;
    --dim: #9a9a9a;
  }
  * { margin: 0; padding: 0; box-sizing: border-box; }
  html, body { width: 842px; height: 1200px; overflow: hidden; background: var(--stage); }
  .canvas { position: relative; width: 842px; height: 1200px; }

  .dimensions { position: absolute; left: 0; top: 0; width: 842px; height: 1200px; }
  .dim-label { font-family: "Montserrat", sans-serif; font-size: 15px; fill: var(--dim); letter-spacing: 0.5px; }

  .counter-wrap {
    position: absolute; left: 56px; top: 448px; width: 760px; height: 342px;
    background: var(--lime); overflow: hidden;
  }
  .backdrop {
    position: absolute; inset: 0;
    background: radial-gradient(ellipse at 55% 35%, var(--lime-light) 0%, var(--lime) 55%, var(--lime-deep) 100%);
  }
  .fold { position: absolute; top: 0; bottom: 0; border-left: 1px dashed var(--guide); }
  .fold--left { left: 152px; }
  .fold--right { left: 608px; }

  .side-mark {
    position: absolute; top: 132px; width: 86px; height: 86px;
    border-radius: 50%; background: var(--white);
  }
  .side-mark--left { left: 33px; }
  .side-mark--right { left: 641px; }

  .front { position: absolute; left: 152px; top: 0; width: 456px; height: 342px; }

  .brand {
    position: absolute; left: 0; right: 0; top: 36px; text-align: center;
    font-family: "Montserrat", sans-serif; font-weight: 500;
    font-size: 44px; letter-spacing: 10px; padding-left: 10px; color: var(--ink); line-height: 1;
  }
  .brand-rule { position: absolute; left: 74px; width: 308px; top: 104px; height: 2px; background: var(--ink); }
  .tagline {
    position: absolute; left: 0; right: 0; top: 122px; text-align: center;
    font-family: "Montserrat", sans-serif; font-weight: 400; font-size: 19px;
    letter-spacing: 4.4px; padding-left: 4px; line-height: 27px; color: var(--ink);
  }

  .services { position: absolute; left: 74px; top: 194px; width: 308px; height: 70px; display: flex; }
  .service { flex: 1; position: relative; text-align: center; }
  .service + .service { border-left: 1.5px solid var(--ink); }
  .service-icon { display: block; margin: 2px auto 0; width: 42px; height: 42px; }
  .service-icon--placeholder { background: rgba(17,17,17,0.12); border-radius: 4px; }
  .service-name {
    position: absolute; left: 0; right: 0; bottom: 0;
    font-family: "Nunito", sans-serif; font-weight: 800; font-size: 13px; color: var(--ink);
  }

  .web-pill {
    position: absolute; left: 127px; top: 287px; width: 202px; height: 24px;
    border-radius: 12px; background: var(--white);
    font-family: "Nunito", sans-serif; font-weight: 800; font-size: 11px; color: var(--ink);
    display: flex; align-items: center; justify-content: center;
  }
</style>
</head>
<body>
<div class="canvas">

  <svg class="dimensions" viewBox="0 0 842 1200" aria-hidden="false">
    <g stroke="var(--dim)" stroke-width="1" fill="none">
      <line x1="58" y1="406" x2="84" y2="406"/><line x1="196" y1="406" x2="206" y2="406"/>
      <line x1="232" y1="406" x2="378" y2="406"/><line x1="466" y1="406" x2="610" y2="406"/>
      <line x1="636" y1="406" x2="646" y2="406"/><line x1="724" y1="406" x2="814" y2="406"/>
      <line x1="57" y1="812" x2="57" y2="850" transform="translate(0,0)"/>
      <line x1="30" y1="450" x2="30" y2="580"/><line x1="30" y1="650" x2="30" y2="788"/>
    </g>
    <g fill="var(--dim)">
      <path d="M56 406 l7 -5 v10z"/><path d="M208 406 l-7 -5 v10z"/><path d="M230 406 l7 -5 v10z"/>
      <path d="M612 406 l-7 -5 v10z"/><path d="M634 406 l7 -5 v10z"/><path d="M816 406 l-7 -5 v10z"/>
      <path d="M30 448 l-5 7 h10z"/><path d="M30 790 l-5 -7 h10z"/>
    </g>
    <text class="dim-label" x="140" y="411" text-anchor="middle">400MM</text>
    <text class="dim-label" x="422" y="411" text-anchor="middle">1200MM</text>
    <text class="dim-label" x="685" y="411" text-anchor="middle">400MM</text>
    <text class="dim-label" x="35" y="615" text-anchor="middle" transform="rotate(-90 35 615)">900MM</text>
  </svg>

  <section class="counter-wrap">
    <div class="backdrop" role="img" aria-label="Faded lime-tinted photo of a chef working in a kitchen"></div>

    <div class="side-mark side-mark--left"></div>
    <div class="side-mark side-mark--right"></div>
    <div class="fold fold--left"></div>
    <div class="fold fold--right"></div>

    <div class="front">
      <h1 class="brand">NORVANE</h1>
      <div class="brand-rule"></div>
      <p class="tagline">FOOD HYGIENE AND<br>HEALTH SAFETY</p>

      <div class="services">
        <div class="service">
          <span class="service-icon service-icon--placeholder" role="img" aria-label="Trainer presenting at a board icon"></span>
          <span class="service-name">Training</span>
        </div>
        <div class="service">
          <span class="service-icon service-icon--placeholder" role="img" aria-label="Consultancy icon with food and checklist"></span>
          <span class="service-name">Consultancy</span>
        </div>
        <div class="service">
          <svg class="service-icon" viewBox="0 0 42 42" role="img" aria-label="Phone with tick">
            <rect x="12" y="3" width="18" height="34" rx="3" fill="none" stroke="var(--ink)" stroke-width="1.6"/>
            <line x1="18" y1="7" x2="24" y2="7" stroke="var(--ink)" stroke-width="1.4"/>
            <path d="M16 20 l4 4 l7 -8" fill="none" stroke="var(--ink)" stroke-width="2.2" stroke-linecap="round" stroke-linejoin="round"/>
          </svg>
          <span class="service-name">Safety App</span>
        </div>
      </div>

      <div class="web-pill">www.norvanesolutions.co.uk</div>
    </div>
  </section>

</div>
</body>
</html>
```